Modern Catering Company needs Letterhead Design

We need a letterhead design that will make effective use of the corporate logo and color scheme, along with careful typography, helps this letterhead design communicate the brand well. We do have a corporate logo, however feel free to enhance the color scheme with gold and purple. We are serving a very upscale clientele so the letterhead has to reflect elegance, professionalism, cleanliness, and modern style. We are branding the company so the letterhead and business cards must fit the brand story. There should be no cartoonish elements in the design and we are looking for sharper lines.

Target Market(s)

Businesses and upscale clientele

Industry/Entity Type

Catering

Contact Information for Business Card

while this design can have any number of quirks and distinctions, it needs to be cohesive with the entire brand story clean, professional but edgy

Requirements
Must have
• must have good and carefully placement of it’s logo and where you place the text or the message. Colors blue, very deep purple, jewel tones not pastels, gold. Blue must be the primary color you may accent with purple or gold. Contact information is as follows: Co-Owners/ Chefs: R. Hollowmere & L. Brandt, phone: 414-555-0182 email:Contact@orchardtablecatering.example, address: 6127 W Larkspur Hollow Rd, Milwaukee, WI 53299
Should not have
• pastel colors, Do not add the BBQ information to the letterhead or business card it was a mistake by the previous designer.

```html
<!DOCTYPE html>
<html lang="en">
<head>
<meta charset="utf-8">
<title>Orchard Table Catering – Stationery</title>
<link href="https://fonts.googleapis.com/css2?family=Montserrat:wght@400;500;600&display=swap" rel="stylesheet">
<style>
:root{
  --brand-blue:#2f5ee0;
  --ink:#2e2e2e;
  --charcoal:#333435;
  --paper:#f2f2f2;
  --stage:#d2d2d4;
  --rule:#d9d9d9;
}
*{box-sizing:border-box;margin:0;padding:0}
html,body{width:1200px;height:1069px;overflow:hidden}
body{background:var(--stage);font-family:'Montserrat',sans-serif;color:var(--ink);position:relative}

.letterhead{position:absolute;left:130px;top:127px;width:631px;height:815px;background:var(--paper);overflow:hidden}
.wordmark{font-family:'Montserrat',sans-serif;font-weight:500;color:var(--brand-blue);line-height:1.05;letter-spacing:.04em;text-transform:uppercase;white-space:nowrap}
.letterhead .wordmark{position:absolute;left:46px;top:100px;font-size:22px}
.contact{position:absolute;left:435px;top:70px;font-size:8.3px;line-height:11px}
.contact li{list-style:none;display:flex;align-items:center;gap:5px}
.contact svg{width:8px;height:8px;flex:none}
.contact address{font-style:normal;margin-top:7px}
.date{position:absolute;left:46px;top:228px;font-size:8.8px}
.recipient{position:absolute;left:46px;top:250px;font-size:8.8px;line-height:11px;font-style:normal}
.letter-body{position:absolute;left:46px;right:47px;top:343px;font-size:8.6px;line-height:11.1px}
.letter-body .salutation{font-weight:600;margin-bottom:11px}
.letter-body p{text-align:justify;margin-bottom:11px}
.signoff{position:absolute;left:46px;top:598px;font-size:8.8px;line-height:11px}
.signoff strong{font-weight:600}
.signature{position:absolute;left:126px;top:594px;width:138px;height:66px;border-radius:6px;background:linear-gradient(135deg,#e3e6f2,#eceef5)}
.wave{position:absolute;left:0;bottom:0;width:100%;display:block}

.card{position:absolute;left:810px;width:261px;height:150px;overflow:hidden}
.card-front{top:272px;background:var(--paper)}
.card-front .wordmark{position:absolute;left:14px;top:60px;font-size:10px;letter-spacing:.02em}
.card-front .divider{position:absolute;left:111px;top:36px;width:1px;height:72px;background:var(--rule)}
.card-details{position:absolute;left:119px;top:34px;font-size:5.6px;line-height:7.6px;white-space:nowrap}
.card-details .names{color:var(--brand-blue);font-weight:600;font-size:6px}
.card-details .role{margin-bottom:6px}
.card-details li{list-style:none;display:flex;align-items:center;gap:3px}
.card-details svg{width:5.5px;height:5.5px;flex:none}
.card-details address{font-style:normal;margin-top:5px}
.card-centered{display:flex;flex-direction:column;align-items:center;justify-content:center;text-align:center}
.card-centered .wordmark{font-size:15px;margin-top:6px}
.card-centered .url{font-size:6.2px;margin-top:26px}
.card-dark{top:461px;background:var(--charcoal)}
.card-dark .url{color:#9a9a9a}
.card-light{top:649px;background:var(--paper)}
</style>
</head>
<body>

<svg width="0" height="0" style="position:absolute" aria-hidden="true">
  <symbol id="icon-phone" viewBox="0 0 10 10"><rect width="10" height="10" rx="2" fill="#2f5ee0"/><path d="M3 2.3l1.2 1.5-.7.7c.4.9 1.1 1.6 2 2l.7-.7L7.7 7 7 7.9C4.6 7.6 2.4 5.4 2.1 3z" fill="#fff"/></symbol>
  <symbol id="icon-mail" viewBox="0 0 10 10"><rect width="10" height="10" rx="2" fill="#2f5ee0"/><rect x="2" y="3" width="6" height="4" fill="none" stroke="#fff" stroke-width=".8"/><path d="M2 3l3 2.3L8 3" fill="none" stroke="#fff" stroke-width=".8"/></symbol>
  <symbol id="icon-web" viewBox="0 0 10 10"><rect width="10" height="10" rx="2" fill="#2f5ee0"/><circle cx="5" cy="5" r="3" fill="none" stroke="#fff" stroke-width=".8"/><path d="M2 5h6M5 2c1.5 1.8 1.5 4.2 0 6M5 2c-1.5 1.8-1.5 4.2 0 6" fill="none" stroke="#fff" stroke-width=".6"/></symbol>
</svg>

<section class="letterhead">
  <div class="wordmark">Orchard Table<br>Catering</div>

  <div class="contact">
    <ul>
      <li><svg><use href="#icon-phone"/></svg>414-555-0182</li>
      <li><svg><use href="#icon-mail"/></svg>contact@orchardtablecatering.example</li>
      <li><svg><use href="#icon-web"/></svg>www.orchardtablecatering.example</li>
    </ul>
    <address>6127 W Larkspur Hollow Rd<br>Milwaukee, WI 53299</address>
  </div>

  <p class="date">30.09.2015</p>
  <address class="recipient">Recipient’s name<br>Lindenweg 4<br>10999 Berlin<br>Germany</address>

  <div class="letter-body">
    <p class="salutation">Dear sir,</p>
    <p>Communication is a very integral part of living creatures, animals and humans. Communication may be verbal or written. Written communication however is only applicable to human beings. Can you even imagine a world without communication? Verbal communication can be through telephones, webcams or in person. Written communication is through letters, emails and mobile phone messages.</p>
    <p>In today’s world of great inventions and technology, letters have somehow become redundant. It is the time for text messages or chats. But they still can communicate a lot more than all other modes of communication. Organizations and various government departments still bank on letters as a strong medium of communication. There is no comparison in costs of sending letters as compared to costs of mobile phone messages though – letters are far cheaper. Letters now commonly known as “hard copy documents” are considered more relevant and important than email copies of text messages as proof or evidence of some sort.</p>
    <p>Letters speak volumes about a person or an organization that writes it. So one must take utmost care ensuring that the language used in any letter is appropriate for the occasion for which it is being written. Since a letter is also a written proof or document, if there are certain things that should not form a part of it, then that too should be carefully handled.</p>
    <p>Writing a good letter is an art. But if for some reason someone is unable to write that perfect letter, these different types of letters provide a base for you to build on. Sample letters have been given for everyone to understand what all information needs to form a part of the letter type and then it can be customized.</p>
  </div>

  <p class="signoff">Yours Sincerely,<br><strong>Jona Verel</strong></p>
  <div class="signature" role="img" aria-label="Handwritten signature in blue ink"></div>

  <svg class="wave" viewBox="0 0 631 50" preserveAspectRatio="none" aria-hidden="true">
    <path d="M0 22C180 4 430-4 631 34V50H0Z" fill="var(--brand-blue)"/>
    <path d="M110 50C300 10 480 6 631 38V50Z" fill="var(--rule)"/>
    <path d="M200 50C370 18 520 14 631 43V50Z" fill="var(--charcoal)"/>
  </svg>
</section>

<section class="card card-front">
  <div class="wordmark">Orchard Table<br>Catering</div>
  <div class="divider"></div>
  <div class="card-details">
    <p class="names">R. HOLLOWMERE &amp; L. BRANDT</p>
    <p class="role">Co-Owners / Chefs</p>
    <ul>
      <li><svg><use href="#icon-phone"/></svg>414-555-0182</li>
      <li><svg><use href="#icon-mail"/></svg>contact@orchardtablecatering.example</li>
      <li><svg><use href="#icon-web"/></svg>www.orchardtablecatering.example</li>
    </ul>
    <address>6127 W Larkspur Hollow Rd<br>Milwaukee, WI 53299</address>
  </div>
  <svg class="wave" viewBox="0 0 261 14" preserveAspectRatio="none" aria-hidden="true">
    <path d="M0 6C80 0 180-1 261 10V14H0Z" fill="var(--brand-blue)"/>
    <path d="M50 14C130 2 200 2 261 11V14Z" fill="var(--rule)"/>
    <path d="M90 14C160 4 220 4 261 12V14Z" fill="var(--charcoal)"/>
  </svg>
</section>

<section class="card card-dark card-centered">
  <div class="wordmark">Orchard Table<br>Catering</div>
  <p class="url">www.orchardtablecatering.example</p>
</section>

<section class="card card-light card-centered">
  <div class="wordmark">Orchard Table<br>Catering</div>
  <p class="url">www.orchardtablecatering.example</p>
</section>

</body>
</html>
```